Visitenkarten-Design für eine Privatpraxis für Physiotherapie
Zielgruppe
Privatpraxis für Physiotherapie
Aufgabenstellung
----- siehe Ausschreibung ------

```html
<!DOCTYPE html>
<html lang="de">
<head>
<meta charset="utf-8">
<title>Visitenkarte – Privatpraxis für Physiotherapie</title>
<link rel="stylesheet" href="https://fonts.googleapis.com/css2?family=Barlow+Condensed:wght@400;500;600;700&family=Share+Tech+Mono&display=swap">
<style>
  :root {
    --stage: #d9cdb4;
    --sun-top: #e9a55a;
    --sun-mid: #f6d79a;
    --sun-low: #e7b383;
    --sea: #c99678;
    --shore: #2a1810;
    --arch: rgba(255, 250, 242, 0.72);
    --gold: #d9ae12;
    --red: #e0361c;
    --ink: #1c1a18;
    --white: #ffffff;
  }
  * { box-sizing: border-box; margin: 0; padding: 0; }
  html, body { width: 1200px; height: 800px; overflow: hidden; }
  body {
    background: var(--stage);
    font-family: "Barlow Condensed", "Arial Narrow", sans-serif;
    color: var(--ink);
    position: relative;
  }
  .card {
    position: absolute;
    top: 120px;
    width: 360px;
    height: 556px;
    overflow: hidden;
    box-shadow: 0 6px 18px rgba(60, 40, 20, 0.18);
  }
  .card--front { left: 208px; }
  .card--back { left: 621px; }
  .card__photo {
    position: absolute; inset: 0;
    background:
      linear-gradient(180deg, var(--sun-top) 0%, var(--sun-mid) 38%, var(--sun-low) 68%, var(--sea) 93%, var(--shore) 94%, var(--shore) 100%);
  }
  .card--front .card__photo::before {
    content: ""; position: absolute; left: 0; top: 22px; bottom: 0; width: 70px;
    background: linear-gradient(90deg, #3a1a0c 0%, rgba(120, 50, 20, 0.85) 55%, rgba(180, 90, 40, 0) 100%);
  }
  .card__arch { position: absolute; inset: 0; width: 100%; height: 100%; }
  .abs { position: absolute; }
  .web {
    top: 16px; display: flex; align-items: center; gap: 5px;
    color: var(--red); font-size: 21px; font-weight: 400; white-space: nowrap;
  }
  .card--front .web { left: 86px; }
  .card--back .web { left: 54px; }
  .web svg { width: 20px; height: 20px; }
  .brand-dot { border-radius: 50%; background: var(--gold); }
  .brand-name {
    color: var(--gold); font-weight: 700; letter-spacing: 0.5px; white-space: nowrap;
    text-align: center; width: 100%;
  }
  .tagline {
    font-family: "Share Tech Mono", monospace; color: var(--red);
    text-align: center; width: 100%; white-space: nowrap;
  }
  .front-center { left: 60px; width: 300px; text-align: center; }
  .address { font-size: 20px; line-height: 25px; }
  .block { left: 86px; font-size: 20px; line-height: 25px; white-space: nowrap; }
  .block__title { font-weight: 600; }
  .hours { left: 86px; top: 429px; font-size: 19px; line-height: 25px; }
  .hours__row { display: flex; white-space: nowrap; }
  .hours__days { color: var(--red); font-weight: 500; width: 80px; }
  .hours__time { width: 150px; text-align: right; }
  .termine-title { left: 40px; top: 199px; font-size: 20px; font-weight: 600; }
  .slot-grid {
    left: 37px; top: 228px; width: 323px;
    display: grid; grid-template-columns: 165px 153px; column-gap: 5px; row-gap: 4px;
  }
  .slot {
    height: 42px; background: var(--white); color: var(--red);
    font-size: 11px; padding: 2px 4px;
  }
  .location {
    left: 38px; top: 464px; font-size: 20px; display: flex; align-items: center; gap: 6px; white-space: nowrap;
  }
  .location svg { width: 14px; height: 20px; }
  .location__sep { margin: 0 6px; }
  .notice {
    left: 40px; top: 491px; width: 300px; color: var(--red);
    font-size: 15px; line-height: 19.5px;
  }
  .notice strong { font-weight: 700; }
</style>
</head>
<body>

<section class="card card--front">
  <div class="card__photo" role="img" aria-label="Foto: Sonnenuntergang am Meer mit Silhouette einer Person"></div>
  <svg class="card__arch" viewBox="0 0 360 556" preserveAspectRatio="none" aria-hidden="true">
    <path d="M360 71 C 230 30, 120 60, 80 190 C 55 260, 52 420, 68 536 L 360 536 Z" fill="var(--arch)"/>
  </svg>

  <div class="abs web">
    <svg viewBox="0 0 20 20" fill="none" stroke="currentColor" stroke-width="1.3"><circle cx="10" cy="10" r="8.5"/><ellipse cx="10" cy="10" rx="4" ry="8.5"/><path d="M1.5 10h17M3 5.5h14M3 14.5h14"/></svg>
    physiotherapie-wendeler.de
  </div>

  <div class="abs brand-dot" style="left:175px; top:95px; width:84px; height:84px;"></div>
  <div class="abs front-center" style="top:198px;">
    <div class="brand-name" style="font-size:29px;">JONAS WENDELER</div>
  </div>
  <div class="abs front-center" style="top:235px;">
    <div class="tagline" style="font-size:10px;">Privatpraxis für Physiotherapie</div>
  </div>
  <div class="abs front-center address" style="top:256px;">
    Lindenhofer Straße 14<br>33790 Halstadt
  </div>

  <div class="abs block" style="top:333px;">
    <div class="block__title">Terminvereinbarung:</div>
    <div>telefonisch&nbsp; 05421 - 30 55 870</div>
  </div>

  <div class="abs block" style="top:404px;">
    <div class="block__title">Öffnungszeiten:</div>
  </div>
  <div class="abs hours">
    <div class="hours__row"><span class="hours__days">Mo|Di|Do</span><span class="hours__time">7:30 Uhr – 11:30 Uhr</span></div>
    <div class="hours__row"><span class="hours__days">Mo|Di</span><span class="hours__time">14:00 Uhr – 17:00 Uhr</span></div>
    <div class="hours__row"><span class="hours__days">Sa</span><span class="hours__time">7:30 Uhr – 12:30 Uhr</span></div>
  </div>
</section>

<section class="card card--back">
  <div class="card__photo" role="img" aria-label="Foto: Sonnenuntergang über dem Meer"></div>
  <svg class="card__arch" viewBox="0 0 360 556" preserveAspectRatio="none" aria-hidden="true">
    <path d="M360 73 C 240 35, 130 40, 70 140 C 20 230, 8 420, 26 536 L 360 536 Z" fill="var(--arch)"/>
  </svg>

  <div class="abs web">
    <svg viewBox="0 0 20 20" fill="none" stroke="currentColor" stroke-width="1.3"><circle cx="10" cy="10" r="8.5"/><ellipse cx="10" cy="10" rx="4" ry="8.5"/><path d="M1.5 10h17M3 5.5h14M3 14.5h14"/></svg>
    physiotherapie-wendeler.de
  </div>

  <div class="abs brand-dot" style="left:174px; top:80px; width:60px; height:60px;"></div>
  <div class="abs" style="left:60px; width:300px; top:155px;">
    <div class="brand-name" style="font-size:20px;">JONAS WENDELER</div>
  </div>
  <div class="abs" style="left:60px; width:300px; top:179px;">
    <div class="tagline" style="font-size:7px;">Privatpraxis für Physiotherapie</div>
  </div>

  <div class="abs termine-title">Ihre nächsten Termine:</div>
  <div class="abs slot-grid">
    <div class="slot">Datum</div><div class="slot">Uhrzeit</div>
    <div class="slot">Datum</div><div class="slot">Uhrzeit</div>
    <div class="slot">Datum</div><div class="slot">Uhrzeit</div>
    <div class="slot">Datum</div><div class="slot">Uhrzeit</div>
    <div class="slot">Datum</div><div class="slot">Uhrzeit</div>
  </div>

  <div class="abs location">
    <svg viewBox="0 0 14 20" fill="none" stroke="currentColor" stroke-width="1.3"><path d="M7 19 C 3 13, 1 10, 1 7 a6 6 0 0 1 12 0 c0 3 -2 6 -6 12z"/><circle cx="7" cy="7" r="2.3"/></svg>
    Lindenhofer Str. 14<span class="location__sep">|</span>33790 Halstadt
  </div>
  <div class="abs notice">
    Sollten Sie an einem Termin verhindert sein, geben Sie bitte rechtzeitig Bescheid. &nbsp;&nbsp;<strong>Telefon:</strong> 05421 - 30 55 870
  </div>
</section>

</body>
</html>
```